Brantley Advisory Group provides support for renewable energy projects to utilities and suppliers

I need a professional looking business card that is both simple and elegant and unique. My clients are mostly large organizations not individuals. I am a consultant with my own company that is small but would like to give clients the impression I am larger. Smart grid, fiber optics, software, field hardware, distribution automation, substation automation, operations, energy storage/batteries, microgrids, customer service, strategy/roadmaps, conservation, Automated Metering Infrastruture (AMI or smart meters) are all areas of focus.

Target Market(s)

Utilities, suppliers, governmental agencies involved in energy. All types of energy especially natural gas and electrical. Especially renewable energy or green projects.

Contact Information for Business Card

Name - Mark Brantley Cell Phone - 425.318.2746 Email - mbrantley@brantleyag-example.com
Company - Brantley Advisory Group (logo) Title - Principal

Font styles to use
Serif
Sans Serif

Colors

Designer to choose colors to be used in the design.

Requirements
Must have
• Simple and professional and powerful.
• Unique/creative design.
Nice to have
• Utilize color scheme to accent logo colors. Maybe some geometric pattern on edge of card with color.
Should not have
• Busy, complicated, traditional

```html
<!DOCTYPE html>
<html lang="en">
<head>
<meta charset="utf-8">
<title>Brantley Advisory Group — Business Card</title>
<link rel="stylesheet" href="https://fonts.googleapis.com/css2?family=Nunito+Sans:ital,wght@0,400;0,800;1,400&display=swap">
<style>
  :root {
    --canvas-bg: #ececec;
    --card-white: #ffffff;
    --brand-blue: #0f0f9f;
    --brand-green: #5b8a3a;
    --text-grey: #9a9a9a;
    --text-white: #ffffff;
    --card-shadow: 0 10px 28px rgba(0, 0, 0, 0.18);
  }
  * { margin: 0; padding: 0; box-sizing: border-box; }
  html, body {
    width: 1200px;
    height: 1200px;
    overflow: hidden;
    background: var(--canvas-bg);
    font-family: "Nunito Sans", "Helvetica Neue", Arial, sans-serif;
  }
  .canvas {
    position: relative;
    width: 1200px;
    height: 1200px;
  }
  .card {
    position: absolute;
    left: 280px;
    width: 640px;
    height: 366px;
    box-shadow: var(--card-shadow);
  }

  /* Front of card */
  .card-front {
    top: 150px;
    background: var(--card-white);
  }
  .front-brand {
    position: absolute;
    left: 44px;
    top: 44px;
    display: flex;
    align-items: center;
    gap: 16px;
  }
  .brand-square {
    width: 44px;
    height: 44px;
    border: 4px solid var(--brand-green);
    border-radius: 5px;
    flex: none;
  }
  .brand-name {
    font-weight: 800;
    font-size: 30px;
    line-height: 1.1;
    letter-spacing: 0.01em;
  }
  .card-front .brand-name { color: var(--brand-blue); }

  .contact-block {
    position: absolute;
    right: 44px;
    bottom: 34px;
    text-align: right;
    color: var(--text-grey);
  }
  .contact-name {
    font-weight: 800;
    font-size: 26px;
    letter-spacing: 0.06em;
    text-transform: uppercase;
  }
  .contact-title {
    font-style: italic;
    font-size: 20px;
    letter-spacing: 0.06em;
    margin-bottom: 10px;
  }
  .contact-line {
    font-size: 17px;
    letter-spacing: 0.06em;
    line-height: 1.75;
  }
  .contact-label { font-weight: 800; margin-right: 6px; }

  /* Back of card */
  .card-back {
    top: 650px;
    background: var(--brand-blue);
  }
  .back-brand {
    position: absolute;
    left: 0;
    right: 0;
    top: 128px;
    display: flex;
    justify-content: center;
    align-items: center;
    gap: 18px;
  }
  .card-back .brand-square { border-color: var(--text-white); width: 48px; height: 48px; }
  .card-back .brand-name { color: var(--text-white); font-size: 34px; }
  .back-website {
    position: absolute;
    left: 0;
    right: 0;
    bottom: 40px;
    text-align: center;
    color: var(--text-white);
    font-weight: 800;
    font-size: 15px;
    letter-spacing: 0.3em;
  }
</style>
</head>
<body>
<main class="canvas">
  <section class="card card-front" aria-label="Business card front">
    <div class="front-brand">
      <span class="brand-square" aria-hidden="true"></span>
      <span class="brand-name">Brantley Advisory Group</span>
    </div>
    <div class="contact-block">
      <p class="contact-name">Mark Brantley</p>
      <p class="contact-title">Principal</p>
      <p class="contact-line"><span class="contact-label">E:</span>mbrantley@brantleyag-example.com</p>
      <p class="contact-line"><span class="contact-label">M:</span>425.318.2746</p>
    </div>
  </section>

  <section class="card card-back" aria-label="Business card back">
    <div class="back-brand">
      <span class="brand-square" aria-hidden="true"></span>
      <span class="brand-name">Brantley Advisory Group</span>
    </div>
    <p class="back-website">www.brantleyag-example.com</p>
  </section>
</main>
</body>
</html>
```